Technology management company looking for a new website with a professional look

Brennick IT is a recently re-branded technology management company that is looking for a website design to match its personalized approach and friendly culture.

We would like to see a specialized, but related, page style for each of our main service offerings of:

• Commercial IT Support (This is our primary focus)
• Commercial Phone Systems (We partner with http://www.voxtrell.com/ for our phone systems)
• Point of Sale Systems (We partner with http://www.tillmora.com/ for our POS systems.
• Web Design
• Hollow Pine Computers (Our residential computer service offering, branded as Hollow Pine Computers)

The Hollow Pine Computers page should be build upon the Hollow Pine Computers logo, the other four pages should be branded as Brennick IT.

These five separate pages should have subtle, yet clearly defined links to one another. They should also each have a Home, Products, Service, and Company in the menu.

The website should have a clean design with professional appeal, but not appear too sterile or uninviting. It needs to have a simple, easy to navigate menu interface along the top. We would also like the site to be mobile friendly.

It should also allow us to easily tie in links to our social media pages (Facebook, LinkedIn, Twitter and Google+) and provide easy access to our contact information from each page.

This is a link to our old website www.hollowpinecomputers.com

We don't currently have copy available. The text and menu design should be easily editable and expandable so we can use the design to fit our copy.

In general we are looking for a concept we can modify to fit our needs.

We need this design to be available with layers in a .psd format.

Target Market(s)

Small to mid-size businesses.

Industry/Entity Type

Information Technology

Number of Pages Required

5+ page

Font styles to use
Sans Serif

Requirements
Must have
• Mobile Friendly
• Professional Type Face
• Unity between all pages
• .PSD Format
Nice to have
• Themed with our logo
Should not have
• Bubbly unprofessional typeface. No comic sans.

```html
<!DOCTYPE html>
<html lang="en">
<head>
<meta charset="utf-8">
<title>Brennick IT — Technology Management Company</title>
<link href="https://fonts.googleapis.com/css2?family=Open+Sans:wght@300;400;600;700;800&display=swap" rel="stylesheet">
<style>
:root{
  --orange:#f26522;
  --ink:#333333;
  --muted:#777777;
  --grey-btn:#dcdcdc;
  --footer:#111111;
  --footer-bar:#050505;
  --white:#ffffff;
}
*{box-sizing:border-box;margin:0;padding:0}
html,body{width:1200px;height:2804px;overflow:hidden;background:var(--white);font-family:"Open Sans",Arial,sans-serif;color:var(--ink)}
.page{position:relative;width:1200px;height:2804px}

/* header */
.site-header{position:absolute;top:0;left:0;width:1200px;height:44px;background:var(--white);display:flex;align-items:center;justify-content:space-between;padding:0 196px 0 190px;z-index:2}
.brand{display:flex;align-items:center;gap:8px;font-weight:700;font-size:24px;color:var(--ink)}
.brand-dot{width:18px;height:18px;border-radius:50%;background:var(--orange)}
.main-nav{display:flex;gap:26px;font-size:11px;font-weight:600;letter-spacing:.5px}
.main-nav a{color:var(--ink);text-decoration:none}
.main-nav a.active{color:var(--orange)}

/* hero */
.hero{position:absolute;top:44px;left:0;width:1200px;height:430px;background:linear-gradient(160deg,#4b5460 0%,#2d3846 45%,#1b2633 100%)}
.hero-title{position:absolute;top:130px;width:100%;text-align:center;color:var(--white);font-size:42px;font-weight:700;line-height:58px;letter-spacing:.5px}
.hero-title .accent{color:var(--orange)}
.scroll-mouse{position:absolute;left:584px;top:310px}

/* intro */
.intro{position:absolute;top:512px;width:100%;text-align:center}
.intro h1{font-size:34px;font-weight:300;color:#555;line-height:40px}
.intro h2{font-size:26px;font-weight:700;letter-spacing:2px;color:var(--ink);line-height:34px;text-transform:uppercase}
.intro p{width:480px;margin:10px auto 0;font-size:12px;line-height:17px;color:var(--muted)}

.services{position:absolute;top:690px;left:180px;display:flex;gap:24px}
.service-card{position:relative;width:150px;height:238px;background:var(--orange)}
.service-card .photo{position:absolute;left:10px;top:0;right:0;height:168px;background:linear-gradient(180deg,#8a9099,#3c4450)}
.service-card .label{position:absolute;left:10px;right:0;bottom:0;height:70px;background:#2a2f36;color:var(--white);font-size:11px;font-weight:700;text-align:center;display:flex;align-items:center;justify-content:center;text-transform:uppercase;line-height:15px;padding:0 8px}

/* newsletter */
.newsletter{position:absolute;top:1020px;left:0;width:1200px;height:140px;background:linear-gradient(90deg,#123a66 0%,#1e5f9c 50%,#123a66 100%)}
.newsletter h3{position:absolute;left:172px;top:30px;color:var(--white);font-size:22px;font-weight:400}
.newsletter .field{position:absolute;left:172px;top:72px;width:680px;height:34px;background:#2e6aa3;color:#c9d9ea;font-size:12px;padding:0 14px;display:flex;align-items:center}
.newsletter .submit{position:absolute;left:866px;top:72px;width:100px;height:34px;background:var(--orange);color:var(--white);font-size:11px;font-weight:700;display:flex;align-items:center;justify-content:center;text-transform:uppercase}

/* features */
.section-head{position:absolute;width:100%;text-align:center}
.section-head .small{font-size:32px;font-weight:300;color:#555;line-height:38px}
.section-head .big{font-size:34px;font-weight:700;color:var(--ink);line-height:40px}
.section-head p{width:460px;margin:8px auto 0;font-size:12px;line-height:17px;color:var(--muted)}
.features{position:absolute;top:1400px;left:184px;display:grid;grid-template-columns:repeat(3,250px);column-gap:40px;row-gap:30px}
.feature{text-align:center}
.feature svg{display:block;margin:0 auto 14px}
.feature .btn{height:70px;background:var(--grey-btn);display:flex;align-items:center;justify-content:center;font-size:17px;font-weight:600;color:var(--ink)}

/* portfolio */
.filters{position:absolute;top:1926px;left:172px;display:flex;gap:22px;font-size:11px;color:var(--muted);align-items:center}
.filters .on{background:var(--orange);color:var(--white);padding:4px 12px;font-weight:600}
.gallery{position:absolute;top:1972px;left:172px;display:grid;grid-template-columns:repeat(3,276px);grid-template-rows:210px 210px;column-gap:16px;row-gap:14px}
.gallery .shot{background:linear-gradient(150deg,#d8d8d8,#6a6a6a)}

/* footer */
.site-footer{position:absolute;top:2448px;left:0;width:1200px;height:304px;background:var(--footer);color:#bbbbbb;font-size:11px}
.footer-col{position:absolute;top:22px}
.footer-col h4{color:var(--white);font-size:12px;font-weight:600;margin-bottom:12px}
.contact-line{display:flex;gap:8px;margin-bottom:12px;line-height:15px}
.contact-line .dot{width:8px;height:8px;border-radius:50%;background:var(--orange);margin-top:3px;flex:none}
.socials{display:flex;gap:6px;margin-top:8px}
.socials span{width:20px;height:20px;border-radius:50%;background:#555}
.input{width:150px;height:22px;background:#2a2a2a;margin-bottom:8px;padding:4px 8px;color:#888;font-size:10px}
.input.tall{height:52px}
.send{width:50px;height:20px;background:var(--orange);color:var(--white);font-size:10px;display:flex;align-items:center;justify-content:center;margin-left:100px}
.post{display:flex;gap:8px;margin-bottom:14px;width:200px}
.post .thumb{width:40px;height:40px;background:linear-gradient(150deg,#888,#333);flex:none}
.post b{color:var(--white);font-weight:600;display:block;margin-bottom:2px}
.post small{color:#888;font-size:9px;line-height:12px;display:block}
.links li{list-style:none;margin-bottom:6px}
.footer-brand{position:absolute;left:950px;top:220px;display:flex;align-items:center;gap:8px;font-weight:700;font-size:24px;color:var(--white)}
.footer-bar{position:absolute;top:2752px;left:0;width:1200px;height:52px;background:var(--footer-bar);color:#888;font-size:10px;display:flex;align-items:center;padding-left:190px}
</style>
</head>
<body>
<div class="page">

<header class="site-header">
  <div class="brand"><span class="brand-dot"></span>Brennick IT</div>
  <nav class="main-nav">
    <a href="#" class="active">HOME</a><a href="#">ABOUT</a><a href="#">SERVICES ▾</a><a href="#">CONTACT US</a>
  </nav>
</header>

<section class="hero" role="img" aria-label="Photo of business people working at a desk with laptops and documents, dark blue tint">
  <h2 class="hero-title">Professional Service <span class="accent">Customized</span><br>To Meet Your <span class="accent">Needs</span></h2>
  <svg class="scroll-mouse" width="32" height="48" viewBox="0 0 32 48"><rect x="2" y="2" width="28" height="44" rx="14" fill="none" stroke="#fff" stroke-width="2"/><rect x="14" y="10" width="4" height="10" rx="2" fill="#f26522"/></svg>
</section>

<section class="intro">
  <h1>We Are Brennick IT</h1>
  <h2>Technology Management Company</h2>
  <p>Smart support for growing offices, with friendly people who know your systems and keep every desk running.</p>
</section>

<div class="services">
  <div class="service-card"><div class="photo" role="img" aria-label="Technician at work on office computers"></div><div class="label">Commercial IT Support</div></div>
  <div class="service-card"><div class="photo" role="img" aria-label="Desk phone system"></div><div class="label">Commercial Phone Systems</div></div>
  <div class="service-card"><div class="photo" role="img" aria-label="Point of sale terminal"></div><div class="label">Point of Sale Systems</div></div>
  <div class="service-card"><div class="photo" role="img" aria-label="Website on a laptop screen"></div><div class="label">Web Design</div></div>
  <div class="service-card"><div class="photo" role="img" aria-label="Home computer repair"></div><div class="label">Hollow Pine Computers</div></div>
</div>

<section class="newsletter">
  <h3>Subscribe to our Newsletter</h3>
  <div class="field">Email</div>
  <div class="submit">Subscribe</div>
</section>

<div class="section-head" style="top:1252px">
  <div class="small">What We Do</div>
  <div class="big">Our Cool Features</div>
  <p>Everything your office needs to stay connected, secure and ready, from the phones to the checkout counter.</p>
</div>

<div class="features">
  <div class="feature">
    <svg width="54" height="48" viewBox="0 0 54 48"><path d="M14 36a11 11 0 0 1 0-22 15 15 0 0 1 28 4 9 9 0 0 1-2 18z" fill="none" stroke="#f26522" stroke-width="3"/><rect x="20" y="22" width="14" height="8" fill="#f26522"/></svg>
    <div class="btn">Software based PBX</div>
  </div>
  <div class="feature">
    <svg width="54" height="48" viewBox="0 0 54 48"><rect x="15" y="4" width="24" height="32" fill="none" stroke="#f26522" stroke-width="3"/><path d="M20 13h14M20 19h14M20 25h10" stroke="#f26522" stroke-width="2"/><circle cx="36" cy="36" r="7" fill="#f26522"/></svg>
    <div class="btn">Easy Management</div>
  </div>
  <div class="feature">
    <svg width="54" height="48" viewBox="0 0 54 48"><rect x="10" y="6" width="16" height="30" rx="3" fill="none" stroke="#f26522" stroke-width="3"/><rect x="30" y="6" width="16" height="30" rx="3" fill="none" stroke="#f26522" stroke-width="3"/><circle cx="18" cy="31" r="1.5" fill="#f26522"/><circle cx="38" cy="31" r="1.5" fill="#f26522"/></svg>
    <div class="btn">Mobility Any Device</div>
  </div>
  <div class="feature">
    <svg width="54" height="48" viewBox="0 0 54 48"><circle cx="27" cy="10" r="6" fill="#f26522"/><circle cx="11" cy="32" r="6" fill="#f26522"/><circle cx="43" cy="32" r="6" fill="#f26522"/><path d="M27 16v8M27 24L13 30M27 24l14 6" stroke="#f26522" stroke-width="2" fill="none"/></svg>
    <div class="btn">Web Conferencing</div>
  </div>
  <div class="feature">
    <svg width="54" height="48" viewBox="0 0 54 48"><rect x="12" y="6" width="30" height="20" fill="none" stroke="#f26522" stroke-width="3"/><rect x="8" y="30" width="38" height="10" fill="#f26522"/></svg>
    <div class="btn">POS Retail System</div>
  </div>
  <div class="feature">
    <svg width="54" height="48" viewBox="0 0 54 48"><path d="M27 4L6 22h6v20h30V22h6z" fill="#f26522"/><rect x="23" y="30" width="8" height="12" fill="#fff"/></svg>
    <div class="btn">Residential</div>
  </div>
</div>

<div class="section-head" style="top:1806px">
  <div class="small" style="font-size:28px">View our</div>
  <div class="big">Portfolio of work</div>
  <p>Recent projects for local clients</p>
</div>

<div class="filters">
  <span class="on">All</span><span>Software Based PBX</span><span>POS Systems</span><span>Mobility</span><span>Web Design</span><span>Management</span>
</div>

<div class="gallery">
  <div class="shot" role="img" aria-label="Office worker using a computer"></div>
  <div class="shot" role="img" aria-label="Hands typing on a laptop"></div>
  <div class="shot" role="img" aria-label="Tablet with charts on a desk"></div>
  <div class="shot" role="img" aria-label="Close-up of a keyboard"></div>
  <div class="shot" role="img" aria-label="Retail shelves with products"></div>
  <div class="shot" role="img" aria-label="Smartphone on a table"></div>
</div>

<footer class="site-footer">
  <div class="footer-col" style="left:220px">
    <h4>Contact Information</h4>
    <div class="contact-line"><span class="dot"></span><span>Address<br>1420 Larkspur Avenue<br>Dunmore, OH 44120</span></div>
    <div class="contact-line"><span class="dot"></span><span>Phone<br>(555) 204-7781</span></div>
    <div class="contact-line"><span class="dot"></span><span>Email<br>hello@brennickit.com</span></div>
    <div class="contact-line"><span class="dot"></span><span>Working Hours<br>Mon - Fri: 8:00 AM - 6:00 PM<br>Sat: 9:00 AM - 1:00 PM</span></div>
    <div class="socials"><span></span><span></span><span></span><span></span></div>
  </div>
  <div class="footer-col" style="left:428px">
    <h4>Quick Contact</h4>
    <div class="input">Name</div>
    <div class="input">Email</div>
    <div class="input tall">Message</div>
    <div class="send">Send</div>
  </div>
  <div class="footer-col" style="left:680px">
    <h4>Our Blog</h4>
    <div class="post"><div class="thumb" role="img" aria-label="Blog post image"></div><div><b>Supported IP Phones: Provisioning tools</b><small>Set up new desk phones in minutes with a few simple steps for your team.</small></div></div>
    <div class="post"><div class="thumb" role="img" aria-label="Blog post image"></div><div><b>Your Website Information</b><small>Keep your site details current so customers can always reach you.</small></div></div>
  </div>
  <div class="footer-col" style="left:936px">
    <h4>Links</h4>
    <ul class="links"><li>Home</li><li>About Us</li><li>Services</li><li>Hollow Pine</li><li>Contact</li></ul>
  </div>
  <div class="footer-brand"><span class="brand-dot"></span>Brennick IT</div>
</footer>
<div class="footer-bar">© Copyright Information Here</div>

</div>
</body>
</html>
```